Mental Health Non-profit Website that takes donations

We are a faith friendly non profit mental health agency. We need an about us section, a section for taking donations, and a place to list all our therapists and a photo of them
Unfortunately, many of our neighbors in Ohio face mental health challenges which harm their quality of life. Thousands of Ohioans experience trauma, addiction, anxiety, and depression, and the negative outcomes of these experiences continue to grow. While we know that data-driven counseling can improve quality of life for those with mental health challenges, many face economic and social barriers to accessing this transformational care.
Lanterns of Calm crosses barriers to mental health care for Ohioans. We are a nonprofit team of counselors dedicated to employing best practices in modes accessible to people of all backgrounds. A trauma-informed, faith-sensitive methodology uniquely equips us to address holistic mental health challenges. Donor support and community partnerships allow us to meet and serve individuals who could not otherwise access professional care.

Please see our case for support below for more information.

Target Market(s)

Those seeking mental health therapy

Industry/Entity Type

Mental Health Non-profit

Coding

Coded - Design and coding required

Colors

Designer to choose colors to be used in the design.

Requirements
Must have
• Our logo colors of navy blue and gold, our logo, about us section, our mission section, a place to accept donations page for all of our therapists and their pictures, and a place for blog posts

```html
<!DOCTYPE html>
<html lang="en">
<head>
<meta charset="utf-8">
<title>Lanterns of Calm — Non Profit Mental Health Agency</title>
<link rel="stylesheet" href="https://fonts.googleapis.com/css2?family=Montserrat:wght@500;600;700&family=Inter:wght@400;500;600&display=swap">
<style>
:root{
  --navy:#0b1d48;
  --navy-deep:#081636;
  --navy-soft:#1a2d5c;
  --gold-light:#f7dc74;
  --gold:#e2b840;
  --gold-dark:#c8962c;
  --ink:#1d2b4f;
  --text:#4d5566;
  --white:#ffffff;
  --line:#d9dde6;
  --gold-grad:linear-gradient(90deg,var(--gold-light),var(--gold) 60%,var(--gold-dark));
}
*{box-sizing:border-box;margin:0;padding:0}
html,body{width:1200px;height:4831px;overflow:hidden}
body{font-family:"Inter",sans-serif;color:var(--text);background:var(--white);position:relative}
.section{position:absolute;left:0;width:1200px;overflow:hidden}
.abs{position:absolute}
h1,h2,h3,.heading,.btn,.eyebrow{font-family:"Montserrat",sans-serif}
.eyebrow{font-size:13px;letter-spacing:4px;font-weight:600;text-transform:uppercase;color:var(--ink)}
.heading{font-weight:600;text-transform:uppercase;color:var(--ink);font-size:40px;line-height:50px}
.btn{display:flex;align-items:center;justify-content:center;background:var(--gold-grad);color:var(--navy);font-weight:700;font-size:13px;text-transform:uppercase;letter-spacing:.3px}
.para{font-size:15.5px;line-height:26.5px}

/* hero */
.hero{top:0;height:741px;background:linear-gradient(100deg,#3d4f5b 0%,#4b5b66 40%,#38434c 70%,#2b333a 100%)}
.hero-photo{left:520px;top:0;width:680px;height:741px;background:radial-gradient(ellipse at 55% 45%,#5b656c 0%,#3b4349 55%,#2a3035 100%)}
.hero-shade{left:0;top:0;width:1200px;height:741px;background:linear-gradient(90deg,rgba(20,30,50,.55),rgba(20,30,50,.1) 55%,rgba(0,0,0,0))}
.brand{left:88px;top:14px;display:flex;flex-direction:column;align-items:center;width:140px}
.brand-mark{width:56px;height:56px;border-radius:50%;background:var(--gold)}
.brand-name{margin-top:8px;font-family:"Montserrat",sans-serif;font-weight:600;font-size:13px;color:var(--gold);text-transform:uppercase;white-space:nowrap}
.top-contact{top:20px;display:flex;align-items:center;gap:12px;color:var(--white)}
.top-contact .ico{width:36px;height:36px;border-radius:50%;background:var(--gold-grad);display:flex;align-items:center;justify-content:center}
.top-contact small{display:block;font-size:12px;opacity:.9}
.top-contact b{font-size:14px;font-weight:600}
.nav{left:281px;top:88px;display:flex;gap:32px;font-family:"Montserrat",sans-serif;font-size:13px;font-weight:600;color:var(--white);text-transform:uppercase}
.nav-donate{left:960px;top:75px;width:150px;height:41px}
.hero-eyebrow{left:88px;top:316px;color:var(--white);font-size:14px}
.hero-title{left:88px;top:340px;font-size:55px;line-height:56px;color:var(--white);font-weight:600;text-transform:uppercase}
.hero-btn{left:88px;top:536px;width:156px;height:51px}
.dots{left:88px;top:663px;display:flex;gap:10px}
.dots i{width:8px;height:8px;border-radius:50%;background:var(--white);display:block}
.dots i:nth-child(2){background:#9aa3ab}

/* help cards */
.help{top:741px;height:439px;background:linear-gradient(90deg,#1c2c54 0%,var(--navy) 40%,var(--navy-deep) 100%)}
.help-card{top:159px;width:298px;height:186px;border:1.5px solid #8d8050;text-align:center;color:var(--white)}
.help-icon{position:absolute;left:101px;top:-50px;width:96px;height:96px;border-radius:50%;background:var(--gold-grad);display:flex;align-items:center;justify-content:center}
.help-card h3{margin-top:75px;font-size:18px;font-weight:500;text-transform:uppercase}
.help-card p{margin:12px auto 0;width:250px;font-size:15px;line-height:26px;color:#c4cbdb}

/* about */
.about{top:1180px;height:654px;background:var(--white)}
.tree{left:84px;top:91px;width:418px;height:469px;background:radial-gradient(ellipse at 50% 40%,#f2d98a 0%,#e0b954 45%,rgba(255,255,255,0) 72%)}

/* donation */
.donate{top:1834px;height:529px;background:linear-gradient(90deg,#6d8d6d 0%,#7c9c7c 45%,#8aa98a 100%)}
.donate-photo{left:0;top:0;width:560px;height:529px;background:radial-gradient(ellipse at 45% 50%,#c9a98a 0%,#9f8269 30%,#6f8e6e 70%)}

/* mission */
.mission{top:2363px;height:628px;background:var(--white)}
.mission-frame{left:833px;top:78px;width:277px;height:343px;border:2px solid #c8ccd6}
.mission-photo{left:613px;top:93px;width:480px;height:441px;background:linear-gradient(120deg,#8a8f6e 0%,#b6a88e 40%,#d9d2c4 70%,#a9b39b 100%)}

/* therapists */
.team{top:2991px;height:656px;background:linear-gradient(180deg,#1b2c55 0%,var(--navy) 55%,#0e1f47 100%)}
.team .eyebrow,.team .heading{color:var(--white);text-align:center;width:1200px;left:0}
.member{top:209px;width:248px;height:263px;border:1px solid #3a4b78}
.member-photo{height:181px;background:linear-gradient(180deg,#e4e4e6,#c9c9cc)}
.member h3{margin-top:19px;text-align:center;color:var(--white);font-size:17px;font-weight:600;text-transform:uppercase}
.member p{text-align:center;color:#b8c1d6;font-size:15px;margin-top:2px}
.team-btn{left:525px;top:508px;width:150px;height:50px}

/* blog */
.blog{top:3647px;height:722px;background:var(--white)}
.blog-photo{top:210px;width:372px;height:259px}
.blog-card{top:403px;width:341px;height:210px;background:var(--white);box-shadow:0 10px 30px rgba(20,30,60,.08);padding:19px 32px 0 32px}
.blog-date{display:flex;align-items:center;gap:8px;font-family:"Montserrat",sans-serif;font-size:12px;font-weight:600;letter-spacing:1.5px;color:var(--ink)}
.blog-card h3{margin-top:10px;font-size:17.5px;line-height:28px;font-weight:700;color:var(--navy);text-transform:uppercase}
.blog-card .btn{margin-top:20px;width:150px;height:51px}

/* footer */
.footer{top:4369px;height:462px;background:var(--navy-deep);color:#aab3c8}
.footer h4{font-family:"Montserrat",sans-serif;font-size:16.5px;font-weight:700;color:var(--white);text-transform:uppercase}
.quick{left:88px;top:79px}
.quick ul{list-style:none;margin-top:20px}
.quick li{font-size:16px;line-height:34.5px}
.foot-brand{left:450px;top:65px;width:230px;display:flex;flex-direction:column;align-items:center}
.foot-brand .brand-mark{width:80px;height:80px}
.foot-brand .brand-name{font-size:16px;margin-top:14px}
.subscribe{left:392px;top:4622px;display:flex}
.subscribe span{width:197px;height:47px;background:var(--white);color:#6b7280;font-size:15px;display:flex;align-items:center;padding-left:12px}
.subscribe .btn{width:148px;height:47px}
.info{left:855px;top:79px}
.info-item{display:flex;gap:16px;margin-top:26px}
.info-item .ico{width:44px;height:44px;border-radius:50%;background:var(--gold-grad);display:flex;align-items:center;justify-content:center;flex:none}
.info-item small{display:block;font-size:15px;line-height:24px}
.info-item b{display:block;font-size:16px;font-weight:500;color:var(--white);line-height:26px}
.socials{left:88px;top:377px;display:flex;gap:8px}
.socials i{width:46px;height:46px;border-radius:50%;background:var(--gold-grad);display:block}
.copyright{right:88px;top:390px;font-size:14px;color:var(--white)}
</style>
</head>
<body>

<section class="section hero">
  <div class="abs hero-photo" role="img" aria-label="Photo of a tired young woman leaning against a wall with her head in her hand"></div>
  <div class="abs hero-shade"></div>
  <div class="abs brand"><span class="brand-mark"></span><span class="brand-name">Lanterns of Calm</span></div>
  <div class="abs top-contact" style="left:643px">
    <span class="ico"><svg width="18" height="18" viewBox="0 0 24 24"><path fill="#0b1d48" d="M6.6 10.8a15 15 0 006.6 6.6l2.2-2.2a1 1 0 011-.25 11.4 11.4 0 003.6.57 1 1 0 011 1V20a1 1 0 01-1 1A17 17 0 013 4a1 1 0 011-1h3.5a1 1 0 011 1c0 1.25.2 2.45.57 3.6a1 1 0 01-.25 1z"/></svg></span>
    <span><small>Call us</small><b>(555) 014-2290</b></span>
  </div>
  <div class="abs top-contact" style="left:833px">
    <span class="ico"><svg width="18" height="18" viewBox="0 0 24 24"><path fill="#0b1d48" d="M3 5h18v14H3z"/><path fill="none" stroke="#f7dc74" stroke-width="1.8" d="M3 6l9 7 9-7"/></svg></span>
    <span><small>Email us</small><b>hello@lanternsofcalm.org</b></span>
  </div>
  <nav class="abs nav"><span>Home</span><span>About us</span><span>Our mission</span><span>Our therapists</span><span>Blog</span><span>Contact us</span></nav>
  <div class="abs btn nav-donate">Donate now</div>
  <p class="abs eyebrow hero-eyebrow">We are a faith friendly</p>
  <h1 class="abs hero-title">Non profit<br>mental health<br>agency</h1>
  <div class="abs btn hero-btn">Contact us</div>
  <div class="abs dots"><i></i><i></i><i></i></div>
</section>

<section class="section help">
  <div class="abs help-card" style="left:131px">
    <div class="help-icon"><svg width="42" height="42" viewBox="0 0 24 24"><rect x="4" y="10" width="16" height="11" rx="1" fill="#0b1d48"/><circle cx="12" cy="6" r="3.5" fill="#0b1d48"/><path d="M12 18l-3-3a1.6 1.6 0 013-2 1.6 1.6 0 013 2z" fill="#f2cf5c"/></svg></div>
    <h3>Give donation</h3><p>Lorem ipsum dolor sit amet con sectetur adipiscing elit sed.</p>
  </div>
  <div class="abs help-card" style="left:452px">
    <div class="help-icon"><svg width="42" height="42" viewBox="0 0 24 24"><circle cx="12" cy="12" r="9" fill="none" stroke="#0b1d48" stroke-width="2"/><path d="M3 12h18M12 3c3 3 3 15 0 18M12 3c-3 3-3 15 0 18" fill="none" stroke="#0b1d48" stroke-width="1.6"/></svg></div>
    <h3>Support us</h3><p>Lorem ipsum dolor sit amet con sectetur adipiscing elit sed.</p>
  </div>
  <div class="abs help-card" style="left:771px">
    <div class="help-icon"><svg width="42" height="42" viewBox="0 0 24 24"><circle cx="9" cy="7" r="4" fill="#0b1d48"/><path d="M2 21c0-5 3-8 7-8s7 3 7 8z" fill="#0b1d48"/><path d="M18 13l-3-3a1.8 1.8 0 013-2.2 1.8 1.8 0 013 2.2z" fill="#0b1d48"/></svg></div>
    <h3>Become a volunteer</h3><p>Lorem ipsum dolor sit amet con sectetur adipiscing elit sed.</p>
  </div>
</section>

<section class="section about">
  <div class="abs tree" role="img" aria-label="Golden tree illustration with round leaves"></div>
  <p class="abs eyebrow" style="left:621px;top:152px">About us</p>
  <h2 class="abs heading" style="left:618px;top:174px">Introducing<br>Lanterns of Calm</h2>
  <p class="abs para" style="left:621px;top:290px;width:450px">Lanterns of Calm is a 501(c)(3) nonprofit organization that offers counseling to Ohioans who cannot access mental health care. We envision a community where all people have healthy relationships, set good boundaries, and enjoy life. To realize this vision, we offer accessible, trauma-informed, and faith-friendly counseling to residents of underprivileged or rural Ohio communities.</p>
  <div class="abs btn" style="left:621px;top:508px;width:150px;height:52px">View more</div>
</section>

<section class="section donate">
  <div class="abs donate-photo" role="img" aria-label="Cupped hands holding an eggshell with a green seedling"></div>
  <p class="abs eyebrow" style="left:600px;top:103px;color:var(--white)">Donation</p>
  <h2 class="abs heading" style="left:598px;top:122px;color:var(--white)">Become a<br>donate now</h2>
  <p class="abs para" style="left:600px;top:238px;width:450px;color:var(--white)">Lorem ipsum dolor sit amet consectetur adipisicing elito sed do eiusmod tempor incididunt ut labore et doloredi magna aliqua. Ut enim ad minim veniam, quis nostrudot exercitation ullamco laboris nisi ut aliquip.</p>
  <div class="abs btn" style="left:600px;top:375px;width:234px;height:50px">Donate now</div>
</section>

<section class="section mission">
  <p class="abs eyebrow" style="left:88px;top:95px">Mission</p>
  <h2 class="abs heading" style="left:88px;top:114px">Our mission</h2>
  <p class="abs para" style="left:88px;top:181px;width:455px">Mental health impacts every element of our daily lives. From the ways that we work to how we relate with our families, mental wellness allows us to be present in the moment and contribute positively to our communities.</p>
  <p class="abs para" style="left:88px;top:316px;width:440px">Unfortunately, many of our neighbors in Ohio face mental health challenges which harm their quality of life. Thousands of Ohioans experience trauma, addiction, anxiety, and depression, and the negative outcomes of these experiences continue to grow.</p>
  <div class="abs btn" style="left:88px;top:481px;width:150px;height:52px">View more</div>
  <div class="abs mission-frame"></div>
  <div class="abs mission-photo" role="img" aria-label="Counselor holding the hands of a young client during a session"></div>
</section>

<section class="section team">
  <p class="abs eyebrow" style="top:97px">Team members</p>
  <h2 class="abs heading" style="top:112px">Our therapists</h2>
  <div class="abs member" style="left:88px"><div class="member-photo" role="img" aria-label="Portrait of therapist Mark Ellison"></div><h3>Mark Ellison</h3><p>Trauma Specialist</p></div>
  <div class="abs member" style="left:347px"><div class="member-photo" role="img" aria-label="Portrait of therapist Rosa Vantine"></div><h3>Rosa Vantine</h3><p>Anxiety Specialist</p></div>
  <div class="abs member" style="left:604px"><div class="member-photo" role="img" aria-label="Portrait of therapist Peter Haldane"></div><h3>Peter Haldane</h3><p>Depression Specialist</p></div>
  <div class="abs member" style="left:862px"><div class="member-photo" role="img" aria-label="Portrait of therapist Clara Wynne"></div><h3>Clara Wynne</h3><p>Trauma Specialist</p></div>
  <div class="abs btn team-btn">View more</div>
</section>

<section class="section blog">
  <p class="abs eyebrow" style="left:0;width:1200px;text-align:center;top:92px">Article</p>
  <h2 class="abs heading" style="left:0;width:1200px;text-align:center;top:104px">Our blog</h2>
  <div class="abs blog-photo" style="left:32px;background:linear-gradient(120deg,#e9e4dc,#b9a88f 50%,#5c4b6e)" role="img" aria-label="Counselor comforting a young man"></div>
  <div class="abs blog-photo" style="left:414px;background:linear-gradient(120deg,#c9ccd1,#8c99a8 50%,#d8d4cc)" role="img" aria-label="Therapist talking with a distressed woman on a sofa"></div>
  <div class="abs blog-photo" style="left:797px;background:linear-gradient(120deg,#e7dcc8,#c7b08c 50%,#8a7a66)" role="img" aria-label="Two women talking in a bright office"></div>
  <div class="abs blog-card" style="left:47px"><div class="blog-date"><svg width="12" height="12" viewBox="0 0 24 24"><rect x="3" y="5" width="18" height="16" fill="#1d2b4f"/><path d="M7 2v5M17 2v5" stroke="#1d2b4f" stroke-width="3"/></svg>15 Nov 2024</div><h3>Ut enim ad minima veniam, quis nostrum exercitatio ullam voluptate vel.</h3><div class="btn">Read more</div></div>
  <div class="abs blog-card" style="left:430px"><div class="blog-date"><svg width="12" height="12" viewBox="0 0 24 24"><rect x="3" y="5" width="18" height="16" fill="#1d2b4f"/><path d="M7 2v5M17 2v5" stroke="#1d2b4f" stroke-width="3"/></svg>15 Nov 2024</div><h3>Ut enim ad minima veniam, quis nostrum exercitatio ullam voluptate vel.</h3><div class="btn">Read more</div></div>
  <div class="abs blog-card" style="left:812px"><div class="blog-date"><svg width="12" height="12" viewBox="0 0 24 24"><rect x="3" y="5" width="18" height="16" fill="#1d2b4f"/><path d="M7 2v5M17 2v5" stroke="#1d2b4f" stroke-width="3"/></svg>15 Nov 2024</div><h3>Ut enim ad minima veniam, quis nostrum exercitatio ullam voluptate vel.</h3><div class="btn">Read more</div></div>
</section>

<footer class="section footer">
  <div class="abs quick"><h4>Quick links</h4><ul><li>Home</li><li>About Us</li><li>Our Mission</li><li>Our Therapists</li><li>Blog</li><li>Contact Us</li></ul></div>
  <div class="abs foot-brand"><span class="brand-mark"></span><span class="brand-name">Lanterns of Calm</span></div>
  <div class="abs info"><h4>Cotact information</h4>
    <div class="info-item"><span class="ico"><svg width="18" height="18" viewBox="0 0 24 24"><path fill="#0b1d48" d="M3 5h18v14H3z"/><path fill="none" stroke="#f7dc74" stroke-width="1.8" d="M3 6l9 7 9-7"/></svg></span><span><small>Email:</small><b>info@lanternsofcalm.org</b></span></div>
    <div class="info-item"><span class="ico"><svg width="18" height="18" viewBox="0 0 24 24"><path fill="#0b1d48" d="M6.6 10.8a15 15 0 006.6 6.6l2.2-2.2a1 1 0 011-.25 11.4 11.4 0 003.6.57 1 1 0 011 1V20a1 1 0 01-1 1A17 17 0 013 4a1 1 0 011-1h3.5a1 1 0 011 1c0 1.25.2 2.45.57 3.6a1 1 0 01-.25 1z"/></svg></span><span><small>Phone:</small><b>(555) 014-2290</b></span></div>
    <div class="info-item"><span class="ico"><svg width="18" height="18" viewBox="0 0 24 24"><path fill="#0b1d48" d="M12 2a7 7 0 00-7 7c0 5 7 13 7 13s7-8 7-13a7 7 0 00-7-7z"/><circle cx="12" cy="9" r="2.5" fill="#f7dc74"/></svg></span><span><small>Address:</small><b>48 Willow Lane, Brightfield<br>OH 40021</b></span></div>
  </div>
  <div class="abs socials"><i></i><i></i><i></i><i></i></div>
  <p class="abs copyright">Copyright © 2024 Lanterns of Calm. All rights reserved.</p>
</footer>
<div class="abs subscribe"><span>Enter Email</span><div class="btn">Subscribe</div></div>

</body>
</html>
```